Wedding "Survival Kit" Bag label

I saw a "Wedding Week Survival Kit" that someone create via this site. They had the same design printed twice (facing opposite directions) on the front of the oversized card and then folded it to top off a bag filled with goodies for their guests. That is what I'm looking to go as well as need help with the design for the card. We are getting married in the Riviera Maya on August 2nd, 2015 and both love very modern designs. Our names are Marisol Tepp and Oskar Velminek.

We would like the label to say something like "Wedding Survival Kit" and have some type of cool, abs tract logo that includes our first names, the location and maybe even the date. Feel free to visit our wedding website for inspiration: www.marisolandoskar-example.com

Industry/Entity Type

Wedding

Font styles to use
Other font styles liked:
• Chalkduster or anything fun

Requirements
Must have
• A fun flare to it!! Bright colors are encouraged!
Should not have
• Traditional boring fonts, or basic design

```html
<!DOCTYPE html>
<html lang="en">
<head>
<meta charset="utf-8">
<title>Wedding Survival Kit Bag Label</title>
<link href="https://fonts.googleapis.com/css2?family=Cabin+Sketch:wght@700&family=Great+Vibes&family=Open+Sans:wght@700&display=swap" rel="stylesheet">
<style>
  :root {
    --page: #ebe9e6;
    --check-light: #e6dccf;
    --check-dark: #c9b6a2;
    --band-green: #9bc23a;
    --band-green-dark: #86ab2c;
    --band-text: #eef5dc;
    --title-orange: #f0a21e;
    --title-green: #a6cc3c;
    --badge-ring: #f3a935;
    --badge-face: #f2f2f2;
    --badge-text: #9a9a9a;
    --ribbon: #f7c25a;
    --ribbon-edge: #d99a2b;
    --ribbon-tail: #a0562a;
    --ribbon-text: #3a2a1a;
  }
  * { margin: 0; padding: 0; box-sizing: border-box; }
  html, body { width: 800px; height: 1200px; overflow: hidden; background: var(--page); }
  .canvas { position: relative; width: 800px; height: 1200px; }

  .label {
    position: absolute; left: 20px; top: 391px; width: 760px; height: 418px;
    overflow: hidden; box-shadow: 0 2px 6px rgba(0,0,0,0.15);
  }
  .label__check {
    position: absolute; inset: 0 0 53px 0;
    background: linear-gradient(135deg, var(--check-light), var(--check-dark) 55%, var(--check-light));
  }
  .label__band {
    position: absolute; left: 0; right: 0; bottom: 0; height: 53px;
    background: linear-gradient(var(--band-green), var(--band-green-dark));
    font-family: "Open Sans", Arial, sans-serif; font-weight: 700; color: var(--band-text);
  }
  .band__place { position: absolute; left: 32px; top: 14px; font-size: 21px; }
  .band__date { position: absolute; right: 42px; top: 4px; font-size: 21px; }
  .band__date .day { font-size: 40px; line-height: 1; }
  .band__date sup { font-size: 20px; vertical-align: 20px; margin-left: 1px; }

  .badge {
    position: absolute; left: 14px; top: 6px; width: 182px; height: 182px;
    border-radius: 50%; background: var(--badge-ring);
    display: flex; align-items: center; justify-content: center;
  }
  .badge__face {
    width: 150px; height: 150px; border-radius: 50%; background: var(--badge-face);
    box-shadow: inset 0 -6px 12px rgba(0,0,0,0.12);
    display: flex; align-items: center; justify-content: center;
    font-family: "Great Vibes", cursive; font-size: 52px; color: var(--badge-text);
  }

  .ribbons { position: absolute; left: 52px; top: 186px; width: 190px; height: 150px; }
  .ribbons svg { position: absolute; inset: 0; }
  .ribbon-text {
    position: absolute; left: 0; width: 160px; text-align: center;
    font-family: "Great Vibes", cursive; color: var(--ribbon-text);
  }
  .ribbon-text--groom { top: 6px; font-size: 27px; }
  .ribbon-text--amp { top: 52px; font-size: 24px; }
  .ribbon-text--bride { top: 92px; font-size: 27px; }

  .title { position: absolute; left: 218px; top: 150px; font-family: "Cabin Sketch", "Comic Sans MS", cursive; font-weight: 700; line-height: 1; }
  .title__lead { display: block; font-size: 48px; color: var(--title-orange); }
  .title__main { display: block; font-size: 64px; color: var(--title-green); margin-top: 2px; white-space: nowrap; }
</style>
</head>
<body>
<main class="canvas">
  <section class="label">
    <div class="label__check" role="img" aria-label="Beige and brown gingham check pattern on aged paper"></div>

    <div class="badge">
      <div class="badge__face">M&amp;O</div>
    </div>

    <div class="ribbons">
      <svg width="190" height="150" viewBox="0 0 190 150" aria-hidden="true">
        <polygon points="90,124 190,124 176,136 190,148 100,148" fill="var(--ribbon-tail)"/>
        <rect x="0" y="0" width="160" height="46" fill="var(--ribbon)" stroke="var(--ribbon-edge)" stroke-width="2"/>
        <rect x="12" y="50" width="136" height="34" fill="var(--ribbon)" stroke="var(--ribbon-edge)" stroke-width="2"/>
        <line x1="24" y1="67" x2="64" y2="67" stroke="var(--ribbon-text)" stroke-width="1.5"/>
        <line x1="96" y1="67" x2="136" y2="67" stroke="var(--ribbon-text)" stroke-width="1.5"/>
        <rect x="0" y="88" width="160" height="40" fill="var(--ribbon)" stroke="var(--ribbon-edge)" stroke-width="2"/>
      </svg>
      <span class="ribbon-text ribbon-text--groom">Oskar Velminek</span>
      <span class="ribbon-text ribbon-text--amp">&amp;</span>
      <span class="ribbon-text ribbon-text--bride">Marisol Tepp</span>
    </div>

    <h1 class="title">
      <span class="title__lead">Wedding</span>
      <span class="title__main">Survival Kit Bag</span>
    </h1>

    <footer class="label__band">
      <span class="band__place">Riviera Maya</span>
      <span class="band__date"><span class="day">2</span><sup>nd</sup> august 2015</span>
    </footer>
  </section>
</main>
</body>
</html>
```